Business Card Design

We need a business card design for a business based in Perth Western Australia. We supply bookkeeping,office systems and procedures. This company is run by professional, vibrant woman which needs to come across when looking at this card.
This includes:
Bookkeeping,BAS,Super,Payroll,Group Certificates,Year End Preparation, Budgets,Planning
Staff training
Office Clean Up, Archiving,New Files and Systems
We would like to see designs that use the colours red mahogony(see Seal attachment), black and ivory
We want a Seal(old fashion wax seal) (see attached) with the letters TL engraved into this ,with our mission statement, 'We leave our mark of excellence'
Updates

Hi to all

Please note that Tidewell Ledgers e mail address should read:  tidewellledgers.wa@brightpost.example
Thanks

Industry/Entity Type

Fashion

Contact Information for Business Card

Tidewell Ledgers
Bookkeeping,Office Systems & Procedures
Perth WA
Greta
MOB: 0452 381 647
e mail: tidewellledgers@brightpost.example

```html
<!DOCTYPE html>
<html lang="en">
<head>
<meta charset="utf-8">
<title>Tidewell Ledgers – Business Card</title>
<link rel="stylesheet" href="https://fonts.googleapis.com/css2?family=Source+Sans+3:wght@400&display=swap">
<style>
  :root {
    --page: #ffffff;
    --card-ivory: #ecdbd7;
    --ink: #141414;
    --mahogany: #7a1416;
    --mahogany-deep: #4e0b0d;
  }
  * { margin: 0; padding: 0; box-sizing: border-box; }
  html, body {
    width: 1200px;
    height: 741px;
    overflow: hidden;
    background: var(--page);
  }
  .canvas {
    position: relative;
    width: 1200px;
    height: 741px;
    font-family: "Source Sans 3", "Myriad Pro", Arial, sans-serif;
    color: var(--ink);
  }
  .card {
    position: absolute;
    left: 44px;
    top: 44px;
    width: 1112px;
    height: 651px;
    background: var(--card-ivory);
  }
  .business-lines {
    position: absolute;
    left: 94px;
    top: 121px;
    font-size: 46px;
    line-height: 62px;
    font-weight: 400;
  }
  .contact-person {
    position: absolute;
    left: 97px;
    top: 369px;
    font-size: 46px;
    line-height: 64px;
  }
  .contact-email {
    position: absolute;
    left: 94px;
    top: 608px;
    font-size: 43px;
    line-height: 1;
  }
  .brand-mark {
    position: absolute;
    left: 875px;
    top: 290px;
    width: 220px;
    display: flex;
    flex-direction: column;
    align-items: center;
    gap: 18px;
  }
  .brand-mark__circle {
    width: 190px;
    height: 190px;
    border-radius: 50%;
    background: var(--mahogany);
  }
  .brand-mark__name {
    font-size: 30px;
    line-height: 1;
    color: var(--mahogany-deep);
    white-space: nowrap;
  }
</style>
</head>
<body>
  <div class="canvas">
    <div class="card">
    </div>

    <div class="business-lines">
      <p>Tidewell Ledgers Bookkeeping,</p>
      <p>Office Systems &amp; Proceduress</p>
      <p>Perth WA</p>
    </div>

    <div class="contact-person">
      <p>Greta MOB:</p>
      <p>0452 381 647</p>
    </div>

    <p class="contact-email">e-mail: tidewellledgers.wa@brightpost.example</p>

    <div class="brand-mark">
      <div class="brand-mark__circle"></div>
      <p class="brand-mark__name">Tidewell Ledgers</p>
    </div>
  </div>
</body>
</html>
```